One page (Bach and front) flyer graphic composition with all content provided

We need, by Sunday evening at the latest term, to have the enclosed page graphically worked. It will be inserted in a Fair Catalog. Dimensions 20x20We enclose logo and picture to include and draft. Don't consider the Power Point we include only to handle you content: take it from here and decide how to paste it in page to your own judgment.DLW is a software company, producing for investment market. image to give: SERIOUS, COMPETENT, STRAIGHT TO THE POINT and, most important, CREDIBLE company

Target Market(s)

Investors

Font styles to use
Serif

Colors
276eb1
0355a3
ffffff

Requirements
Must have
• Clear, strong Logo in the front page
• The picture on the back
Nice to have
• Credibility, space, clearness
Should not have
• Confusion, too much "loud"

```html
<!DOCTYPE html>
<html lang="en">
<head>
<meta charset="utf-8">
<title>DLW Fair Catalog Flyer</title>
<link href="https://fonts.googleapis.com/css2?family=Montserrat:ital,wght@0,400;0,500;0,600;0,700;0,800;1,500&display=swap" rel="stylesheet">
<style>
  :root {
    --blue-mid: #276eb1;
    --blue-deep: #0355a3;
    --blue-bright: #1a6fd6;
    --white: #ffffff;
    --black: #000000;
    --backdrop: #d3d4d6;
  }
  html, body { margin: 0; padding: 0; overflow: hidden; }
  body {
    width: 1200px; height: 1200px;
    background: var(--backdrop);
    position: relative;
    font-family: "Montserrat", Arial, sans-serif;
    color: var(--white);
  }
  .page {
    position: absolute;
    width: 600px; height: 600px;
    background: var(--black);
    box-shadow: 0 6px 18px rgba(0,0,0,.35);
    overflow: hidden;
  }
  .page--front { left: 60px; top: 60px; z-index: 2; }
  .page--back { left: 540px; top: 540px; z-index: 1; }

  .abs { position: absolute; }

  /* front */
  .site-url { top: 30px; left: 0; width: 100%; text-align: center; font-weight: 700; font-size: 14px; }
  .brand { top: 58px; left: 0; width: 100%; display: flex; justify-content: center; align-items: center; gap: 18px; }
  .brand__dot { width: 82px; height: 82px; border-radius: 50%; background: var(--blue-bright); }
  .brand__name { font-weight: 800; font-size: 96px; line-height: 1; color: var(--blue-bright); letter-spacing: 2px; }
  .brand__tag { top: 160px; left: 0; width: 100%; text-align: center; font-weight: 600; font-size: 15px; letter-spacing: 3px; color: var(--blue-bright); }

  .heading { font-weight: 700; font-size: 20px; letter-spacing: .5px; }
  .heading--growth { top: 190px; left: 0; width: 100%; text-align: center; }

  .info-box { background: var(--blue-mid); font-size: 11px; line-height: 1.4; padding: 26px 14px 10px; box-sizing: border-box; }
  .info-box--need { top: 232px; left: 28px; width: 270px; height: 70px; }
  .info-box--problem { top: 232px; left: 308px; width: 270px; height: 70px; }
  .tab { background: var(--blue-deep); font-weight: 700; font-size: 12px; padding: 5px 16px 5px 10px; clip-path: polygon(0 0, 88% 0, 100% 100%, 0 100%); }
  .tab--need { top: 224px; left: 20px; }
  .tab--problem { top: 216px; left: 486px; clip-path: polygon(12% 0, 100% 0, 100% 100%, 0 100%); padding: 5px 10px 5px 18px; }

  .heading--solutions { top: 318px; left: 28px; }
  .sol-box { background: var(--blue-deep); font-size: 11px; line-height: 1.3; text-align: center; display: flex; align-items: center; justify-content: center; box-sizing: border-box; padding: 4px 8px; }
  .sol-box--systems { top: 350px; left: 28px; width: 185px; height: 50px; }
  .sol-plus { top: 348px; left: 216px; font-size: 40px; font-weight: 800; color: var(--blue-bright); line-height: 1; }
  .sol-arrow { top: 330px; left: 246px; width: 170px; height: 80px; }
  .sol-arrow__text { top: 350px; left: 252px; width: 140px; height: 44px; font-size: 10.5px; line-height: 1.3; text-align: center; display: flex; align-items: center; justify-content: center; }
  .sol-box--system { top: 316px; left: 424px; width: 156px; height: 84px; flex-direction: column; font-size: 9.5px; }
  .sol-box--system strong { font-size: 11px; font-weight: 700; }

  .heading--have { top: 420px; left: 28px; font-size: 18px; }
  .benefits { top: 448px; left: 28px; width: 552px; display: grid; grid-template-columns: 172px 1fr 1fr; gap: 5px; }
  .benefit-label { background: var(--blue-deep); border-radius: 22px 0 0 22px; font-weight: 700; font-size: 16px; height: 42px; display: flex; align-items: center; justify-content: center; }
  .benefit-cell { background: var(--blue-mid); font-size: 10.5px; line-height: 1.3; text-align: center; height: 42px; display: flex; align-items: center; justify-content: center; padding: 0 6px; }
  .benefit-cell--end { border-radius: 0 22px 22px 0; }

  /* back */
  .photo { top: 0; right: 0; width: 420px; height: 600px;
    background: radial-gradient(ellipse at 55% 32%, #c9a456 0%, #7a6236 22%, #2a2418 48%, #000 72%); }
  .ice-photo { top: 450px; left: 40px; width: 90px; height: 80px; border-radius: 12px;
    background: radial-gradient(circle, #c8c8d0 0%, #555 50%, #000 100%); }
  .back-tagline { top: 300px; left: 50px; font-style: italic; font-weight: 500; font-size: 26px; color: var(--blue-bright); }
  .back-copy { top: 350px; left: 50px; font-size: 16px; line-height: 1.25; }
  .back-copy p { margin: 0 0 10px; }
</style>
</head>
<body>
  <section class="page page--front">
    <div class="abs site-url">www.dlwinvest.io</div>
    <div class="abs brand"><span class="brand__dot"></span><span class="brand__name">DLW</span></div>
    <div class="abs brand__tag">DLW Invest</div>

    <h2 class="abs heading heading--growth" style="margin:0">YOUR MONEY GROWTH</h2>

    <div class="abs info-box info-box--need">Most of us would prefer a major return on our investments.</div>
    <div class="abs tab tab--need">NEED</div>
    <div class="abs info-box info-box--problem">Most of us lacks instruments, know-how and time to do it by ourselves. Moreover, external aid has often been disappointing.</div>
    <div class="abs tab tab--problem">PROBLEM</div>

    <h2 class="abs heading heading--solutions" style="margin:0">DLW SOLUTIONS</h2>
    <div class="abs sol-box sol-box--systems">Utilize most efficient and tested Trading Systems</div>
    <div class="abs sol-plus">+</div>
    <svg class="abs sol-arrow" viewBox="0 0 170 80" aria-hidden="true">
      <polygon points="0,18 135,18 135,0 170,40 135,80 135,62 0,62" fill="var(--blue-deep)"/>
    </svg>
    <div class="abs sol-arrow__text">Adding its own Sentiment Index created for first time on blockchain</div>
    <div class="abs sol-box sol-box--system"><strong>ATLAS</strong>Highly Advanced Trading System<br>Offers major results<br>with a turnkey solution</div>

    <h2 class="abs heading heading--have" style="margin:0">WITH ATLAS YOU CAN HAVE:</h2>
    <div class="abs benefits">
      <div class="benefit-label">BETTER ROI</div>
      <div class="benefit-cell">TODAY machines work better than humans</div>
      <div class="benefit-cell benefit-cell--end">ANYHOW, DLW maintains Human Control OVER machines</div>
      <div class="benefit-label">BETTER VISION</div>
      <div class="benefit-cell">Sentiment Index finds out what people REALY thinks</div>
      <div class="benefit-cell benefit-cell--end">Sentiment + Data = Unbeatable know how</div>
      <div class="benefit-label">MINOR RISK</div>
      <div class="benefit-cell">ATLAS is founded on proven, real numbers</div>
      <div class="benefit-cell benefit-cell--end">Risk and Return are known before, not after</div>
    </div>
  </section>

  <section class="page page--back">
    <div class="abs photo" role="img" aria-label="Photograph of a martini glass filled with gold and silver coins and ice cubes"></div>
    <div class="abs ice-photo" role="img" aria-label="Photograph of a single ice cube"></div>
    <div class="abs back-tagline">We are waiting for you!</div>
    <div class="abs back-copy">
      <p>Ask your invitation to our DLW Hostess<br>and be welcomed to:</p>
      <p>Presidential Suite<br>Level 18</p>
    </div>
  </section>
</body>
</html>
```